Top of the line business card design needed for real estate brokerage

We currently have a business card with our logo but would like to have a revised version. We would love for you to implement your own design that will catch anyone's attention. The theme colors should be black, royal blue, gray/silver, and white.The contact information should be the same as the info on our current business card (picture attached). In the design that we pick, we will need to be able to edit the text so that we can customize the text content for each of our agents. Same goes for the professional picture. There should be an area on the card that each agent can have their professional portrait attached. Please include a version without the picture option as well for agents that do not wish to have a professional picture attached.

```html
<!DOCTYPE html>
<html lang="en">
<head>
<meta charset="utf-8">
<title>Clear Harbor Realty – Business Card</title>
<link rel="stylesheet" href="https://fonts.googleapis.com/css2?family=Open+Sans:wght@400;600;700&display=swap">
<style>
  :root {
    --page-bg: #e9e9ea;
    --card-white: #f3f3f3;
    --ink-black: #1f1f1f;
    --charcoal: #232323;
    --royal-blue: #1f5aa6;
    --deep-blue: #2f4fb0;
    --sky-blue: #3fa7e0;
    --silver: #a9a9a9;
    --text-white: #ffffff;
    --text-soft: #e6e6e6;
  }
  * { box-sizing: border-box; margin: 0; padding: 0; }
  html, body {
    width: 1200px; height: 831px; overflow: hidden;
    background: var(--page-bg);
    font-family: "Open Sans", Arial, sans-serif;
  }
  .canvas {
    position: relative; width: 1200px; height: 831px;
    display: flex; justify-content: center; align-items: center; gap: 40px;
  }
  .card {
    position: relative; width: 540px; height: 327px; overflow: hidden;
    background: var(--card-white);
    box-shadow: 0 6px 18px rgba(0,0,0,0.12);
  }
  .card-art { position: absolute; inset: 0; width: 100%; height: 100%; }

  /* Front */
  .brand {
    position: absolute; left: 0; right: 0; top: 92px;
    display: flex; justify-content: center; align-items: center; gap: 10px;
  }
  .brand-mark { width: 16px; height: 16px; background: var(--royal-blue); }
  .brand-name {
    font-size: 26px; font-weight: 700; color: var(--ink-black); letter-spacing: 0.2px;
  }
  .services {
    position: absolute; left: 0; right: 0; top: 248px;
    display: grid; grid-template-columns: 236px 1px 1fr; row-gap: 16px; column-gap: 36px;
    padding-left: 62px; color: var(--text-white);
    font-size: 14px; font-weight: 700;
  }
  .services .divider { width: 1px; height: 16px; background: var(--text-white); align-self: center; }

  /* Back */
  .card-back { background: var(--card-white); }
  .agent { position: absolute; left: 60px; top: 66px; color: var(--text-white); }
  .agent-name { font-size: 19px; font-weight: 700; letter-spacing: 0.5px; }
  .agent-title { font-size: 14px; color: var(--text-soft); margin-left: 16px; margin-top: -2px; }
  .contact-list { position: absolute; left: 44px; top: 142px; list-style: none; color: var(--text-white); font-size: 13.5px; }
  .contact-list li { display: flex; align-items: flex-start; gap: 14px; height: 35px; }
  .contact-list svg { width: 15px; height: 15px; flex: none; margin-top: 2px; fill: var(--text-white); }
  .contact-list .address { line-height: 18px; }
  .back-brand {
    position: absolute; right: 24px; top: 248px;
    font-size: 19px; font-weight: 700; color: var(--ink-black);
  }
</style>
</head>
<body>
<main class="canvas">

  <section class="card card-front" aria-label="Card front">
    <svg class="card-art" viewBox="0 0 540 327" aria-hidden="true">
      <path d="M0 220 Q270 140 540 220 L540 327 L0 327 Z" fill="var(--ink-black)"/>
      <path d="M0 235 Q270 171 540 235 L540 327 L0 327 Z" fill="var(--royal-blue)"/>
      <path d="M0 229 Q270 158 540 229" fill="none" stroke="var(--text-white)" stroke-width="3"/>
    </svg>
    <div class="brand">
      <span class="brand-mark"></span>
      <span class="brand-name">Clear Harbor Realty</span>
    </div>
    <div class="services">
      <span>Residental Real Estate</span><span class="divider"></span><span>Commercial Real Estate</span>
      <span>Property Management</span><span class="divider"></span><span>Investments</span>
    </div>
  </section>

  <section class="card card-back" aria-label="Card back">
    <svg class="card-art" viewBox="0 0 540 327" aria-hidden="true">
      <path d="M0 0 H478 L268 282 L300 327 H0 Z" fill="var(--charcoal)"/>
      <path d="M478 0 H492 L284 284 L316 327 H300 L268 282 Z" fill="var(--deep-blue)"/>
      <path d="M492 0 H504 L298 286 L330 327 H316 L284 284 Z" fill="var(--sky-blue)"/>
    </svg>
    <div class="agent">
      <p class="agent-name">MR. MARCUS VALE</p>
      <p class="agent-title">Managing Director</p>
    </div>
    <ul class="contact-list">
      <li>
        <svg viewBox="0 0 24 24"><path d="M6.6 10.8a15.1 15.1 0 0 0 6.6 6.6l2.2-2.2a1 1 0 0 1 1-.25 11.4 11.4 0 0 0 3.6.57 1 1 0 0 1 1 1V20a1 1 0 0 1-1 1A17 17 0 0 1 3 4a1 1 0 0 1 1-1h3.5a1 1 0 0 1 1 1c0 1.25.2 2.45.57 3.6a1 1 0 0 1-.25 1z"/></svg>
        <span>555-014-2291</span>
      </li>
      <li>
        <svg viewBox="0 0 24 24"><path d="M3 5h18v14H3z M3 5l9 7 9-7" fill="none" stroke="var(--text-white)" stroke-width="0"/><path d="M3 5h18v2l-9 6-9-6z M3 9l9 6 9-6v10H3z"/></svg>
        <span>mvale@clearharbor.com</span>
      </li>
      <li>
        <svg viewBox="0 0 24 24"><circle cx="12" cy="12" r="9" fill="none" stroke="var(--text-white)" stroke-width="2"/><path d="M3 12h18M12 3c3 3 3 15 0 18M12 3c-3 3-3 15 0 18" fill="none" stroke="var(--text-white)" stroke-width="1.6"/></svg>
        <span>www.clearharborrealty.com</span>
      </li>
      <li>
        <svg viewBox="0 0 24 24"><path d="M12 3 2 12h3v8h5v-6h4v6h5v-8h3z"/></svg>
        <span class="address">2400 Harbor View Blvd,suite310<br>Lakeside Bay,fl 30410</span>
      </li>
    </ul>
    <p class="back-brand">Clear Harbor Realty</p>
  </section>

</main>
</body>
</html>
```